Design Business Card and some Stationery for VoltaCore

Our trademark is VoltaCore.

We manufacture/sell turn-key projects for energy generation (solar, gas etc.)

Our clients are mainly large corporate project managers and higher.
Ideology should be clean, simple and professional.

Required designs:
business cards
A4 portrait
A4 landscape
A5 portrait memo
compliment slip

Info:
All information will be written in Russian, explanations should be with images, thus not tel. but picture of telephone etc)
Saryarka 14, 3rd. floor, 010027 Kazakhstan
Mobile numbers are formatted as this: +7 701 9876543, fax/tel not present.

Logo will be black text on white background (not red/black/white like in attached image, font file included)

```html
<!DOCTYPE html>
<html lang="ru">
<head>
<meta charset="utf-8">
<title>VoltaCore — business card</title>
<link rel="stylesheet" href="https://fonts.googleapis.com/css2?family=Open+Sans:wght@400;600&display=swap">
<style>
  :root {
    --stage: #262626;
    --card-top: #4a4a4a;
    --card-bottom: #222222;
    --text: #f2f2f2;
    --muted: #c9c9c9;
    --rule: #bdbdbd;
  }
  * { margin: 0; padding: 0; box-sizing: border-box; }
  html, body { width: 1200px; height: 901px; overflow: hidden; }
  body {
    background: var(--stage);
    font-family: "Open Sans", sans-serif;
    color: var(--text);
    position: relative;
  }
  .card {
    position: absolute;
    top: 290px;
    width: 520px;
    height: 320px;
    border-radius: 22px;
    background: linear-gradient(160deg, var(--card-top), var(--card-bottom));
    overflow: hidden;
  }
  .card--front { left: 50px; }
  .card--back { left: 630px; }

  .brand {
    position: absolute;
    font-weight: 600;
    letter-spacing: 3px;
    color: var(--text);
    line-height: 1;
  }
  .card--front .brand { left: 36px; top: 70px; font-size: 44px; }
  .card--back .brand { left: 60px; top: 118px; font-size: 54px; }

  .rule {
    position: absolute;
    height: 1px;
    background: var(--rule);
  }
  .card--front .rule { left: 36px; right: 30px; top: 150px; }
  .card--back .rule { left: 220px; right: 30px; top: 268px; }

  .person {
    position: absolute;
    right: 30px;
    top: 100px;
    text-align: right;
  }
  .person__name { font-size: 20px; font-weight: 600; line-height: 1.1; }
  .person__role { font-size: 13px; color: var(--muted); margin-top: 12px; }

  .address {
    position: absolute;
    right: 30px;
    top: 182px;
    text-align: right;
    font-size: 13px;
    line-height: 1.6;
    color: var(--muted);
  }

  .contacts {
    position: absolute;
    left: 36px;
    bottom: 32px;
    list-style: none;
    font-size: 13px;
    line-height: 1.65;
    color: var(--muted);
  }
  .contacts li { display: flex; align-items: center; gap: 10px; }
  .contacts svg { width: 11px; height: 11px; flex: none; }

  .website {
    position: absolute;
    left: 36px;
    top: 256px;
    font-size: 17px;
    color: var(--muted);
    letter-spacing: 0.5px;
  }
</style>
</head>
<body>
  <section class="card card--front" aria-label="Business card front">
    <div class="brand">VOLTACORE</div>
    <div class="person">
      <div class="person__name">Arman Beketov</div>
    </div>
    <div class="rule"></div>
    <div class="person" style="top:158px">
      <div class="person__role" style="margin-top:0">Managing Partner</div>
    </div>
    <div class="address">
      Saryarka 14, 3rd. floor,<br>010027 Kazakhstan
    </div>
    <ul class="contacts">
      <li>
        <svg viewBox="0 0 12 12" aria-hidden="true"><rect x="2.5" y="0.5" width="7" height="11" rx="1.5" fill="none" stroke="#c9c9c9"/><circle cx="6" cy="9.5" r="0.8" fill="#c9c9c9"/></svg>
        +7 701 9876543
      </li>
      <li>
        <svg viewBox="0 0 12 12" aria-hidden="true"><rect x="0.5" y="2" width="11" height="8" fill="#c9c9c9"/><path d="M0.5 2 L6 6.5 L11.5 2" fill="none" stroke="#262626"/></svg>
        name@voltacore.kz
      </li>
      <li>
        <svg viewBox="0 0 12 12" aria-hidden="true"><circle cx="6" cy="6" r="5.5" fill="#c9c9c9"/><path d="M0.5 6 H11.5 M6 0.5 C3 3.5 3 8.5 6 11.5 M6 0.5 C9 3.5 9 8.5 6 11.5" fill="none" stroke="#262626" stroke-width="0.8"/></svg>
        www.voltacore.kz
      </li>
    </ul>
  </section>

  <section class="card card--back" aria-label="Business card back">
    <div class="brand">VOLTACORE</div>
    <div class="website">www.voltacore.kz</div>
    <div class="rule"></div>
  </section>
</body>
</html>
```